Kestrel Summit 2019 Enemies of the End-Times Church Flyer

We want a church conference flyer designed. We are looking for a professional, yet catchy design that uses our brand colors and logo creatively while communicating key information of the event effectively. <br/>The flyer must include all of the following:<br/>Title: Kestrel Summit 2019<br/>Topic: The Enemies of The End-Times Church <br/>Subtitles: <br/> -How the antichrist raises an army by social behavior engineering. <br/>-How the architects of modern social constructs escaped the church's radar. <br/>-The Holy Spirit's end-times agenda:<br/> The Knock-Out Punch!<br/>Speaker: Prophet Marcus Toliver <br/>Dates/time: December 27, 28 & 29 at 6pm<br/>Location: Halvorn Community Center <br/> 241 Pellham Street <br/> Portland, ME 04102<br/>Contact info: phone: 207-555-0148 <br/>email: contact@brookmeadow.example <br/> www.vutel.example<br/>*The flyer must also include a picture of the speaker and our Vutel logo <br/>Thanks, we look forward to seeing what you come up with!

Colors

Designer to choose colors to be used in the design.

Requirements
Must have
• The flyer must include all of the following:
• Title: Kestrel Summit 2019
• Topic: The Enemies of The End-Times Church
• Subtitles:
• -How the antichrist raises an army by social behavior engineering.
• -How the architects of modern social constructs escaped the church's radar.
• -The Holy Spirit's end-times agenda:
• The Knock-Out Punch!
• Speaker: Prophet Marcus Toliver
• Dates/time: December 27, 28 & 29 at 6pm
• Location: Halvorn Community Center
• 241 Pellham Street
• Portland, ME 04102
• Contact info: phone: 207-555-0148
• email: contact@brookmeadow.example
• www.vutel.example
• *The flyer must also include a picture of the speaker and our Vutel logo
Should not have
• Pictures of crosses or church buildings

```html
<!DOCTYPE html>
<html lang="en">
<head>
<meta charset="utf-8">
<title>Kestrel Summit 2019 – The Enemies of The End-Times Church</title>
<link rel="stylesheet" href="https://fonts.googleapis.com/css2?family=Cinzel:wght@700&family=Rajdhani:wght@400;500&display=swap">
<style>
  :root {
    --navy: #003369;
    --orange: #f39019;
    --steel: #6384ad;
    --white: #ffffff;
    --photo-dark: #3a3a3a;
    --photo-light: #b5b5b5;
  }
  * { margin: 0; padding: 0; box-sizing: border-box; }
  html, body { width: 846px; height: 1200px; overflow: hidden; background: var(--navy); }
  .flyer {
    position: relative;
    width: 846px;
    height: 1200px;
    background: var(--navy);
    color: var(--white);
    font-family: "Rajdhani", sans-serif;
    overflow: hidden;
  }
  .event-title, .event-topic, .event-dates {
    position: absolute;
    left: 58px;
    font-family: "Cinzel", serif;
    font-weight: 700;
    white-space: nowrap;
    line-height: 1;
  }
  .event-title { top: 55px; font-size: 34px; letter-spacing: 0.5px; }
  .event-topic { top: 98px; font-size: 33.5px; color: var(--orange); letter-spacing: 0.6px; }
  .event-dates { top: 146px; font-size: 25px; font-weight: 700; letter-spacing: 0.3px; }

  .session {
    position: absolute;
    left: 58px;
    font-size: 26px;
    font-weight: 400;
    line-height: 38px;
    letter-spacing: 0.6px;
    display: flex;
  }
  .session-mark { color: var(--orange); font-weight: 500; white-space: nowrap; }
  .session-one { top: 223px; }
  .session-one .session-mark { width: 36px; }
  .session-two { top: 322px; }
  .session-two .session-mark { width: 69px; }
  .session-three { top: 421px; }
  .session-three .session-mark { width: 102px; }

  .speaker-photo {
    position: absolute;
    left: 58px;
    top: 540px;
    width: 486px;
    height: 325px;
    background: linear-gradient(135deg, var(--photo-light) 0%, #8a8a8a 45%, var(--photo-dark) 100%);
  }
  .speaker-name {
    position: absolute;
    left: 58px;
    top: 881px;
    font-size: 27px;
    letter-spacing: 0.5px;
  }
  .venue {
    position: absolute;
    left: 58px;
    top: 1000px;
    font-size: 27px;
    line-height: 37.5px;
    letter-spacing: 0.8px;
    font-style: normal;
  }
  .organizer {
    position: absolute;
    left: 552px;
    top: 985px;
    width: 200px;
    text-align: center;
  }
  .brand-name {
    font-family: "Cinzel", serif;
    font-weight: 700;
    font-size: 46px;
    line-height: 1;
    letter-spacing: 1px;
  }
  .contact {
    margin-top: 28px;
    font-size: 20px;
    line-height: 29px;
    font-style: normal;
  }
</style>
</head>
<body>
<main class="flyer">
  <h1 class="event-title">Kestrel Summit 2019</h1>
  <h2 class="event-topic">The Enemies of The End-Times Church</h2>
  <p class="event-dates">December 27, 28 &amp; 29 at 6pm</p>

  <p class="session session-one"><span class="session-mark">//</span><span>How the antichrist raises an army<br>by social behavior engineering.</span></p>
  <p class="session session-two"><span class="session-mark">/////</span><span>How the architects of modern social<br>constructs escaped the church‘s radar.</span></p>
  <p class="session session-three"><span class="session-mark">////////</span><span>The Holy Spirit‘s end-times agenda:<br>The Knock-Out Punch!</span></p>

  <div class="speaker-photo" role="img" aria-label="Black and white photo of the speaker preaching"></div>
  <p class="speaker-name">Speaker: Prophet Marcus Toliver</p>

  <address class="venue">
    Location:<br>
    Halvorn Community Center<br>
    241 Pellham Street<br>
    Portland, ME 04102
  </address>

  <div class="organizer">
    <p class="brand-name">VUTEL</p>
    <address class="contact">
      207-555-0148<br>
      contact@brookmeadow.example<br>
      www.vutel.example
    </address>
  </div>
</main>
</body>
</html>
```